Business Card & Stationary Design Project

We are looking for some creative direction for business cards and our stationary.

We are a global logistics firm that has recently changed its name to Marrick Global Logistics and we have a new website due out tomorrow (www.marrick.com.au).

The colours of the company are rich navy tones, I would like to have business cards that fit together to make one picture on the back (possibly an old map of the world??), and the front to be modern contemporary looking.

But I am open to suggestions, so just incorporate our new logo and get going!
Updates

Hi Everyone,

Thank you for all of your designs so far and the time you have put into it.

I have asked many of you for amendments to see if we can get a final product, so with this in mind I am extending the deadline by a few days.

Good luck and thank you once again.

Please message me direct if you need any clarification.

Kind Regards
Colin

Reason: As outlined the extra 3 days is for amendments and changes to the current submissions. Thanks Colin

Industry/Entity Type

Business

```html
<!DOCTYPE html>
<html lang="en">
<head>
<meta charset="utf-8">
<title>Marrick Global Logistics – Business Card</title>
<link href="https://fonts.googleapis.com/css2?family=Arimo:wght@400;700&display=swap" rel="stylesheet">
<style>
  :root {
    --backdrop: #d9dee3;
    --navy-deep: #2e3f8f;
    --navy: #2f5aa6;
    --sky: #3a93d2;
    --sky-light: #55b6e6;
    --ink-light: #ffffff;
    --ink-soft: #dfe9f7;
    --rule: rgba(255, 255, 255, 0.85);
    --orb: #2c6fc0;
  }
  * { margin: 0; padding: 0; box-sizing: border-box; }
  html, body {
    width: 1200px;
    height: 960px;
    overflow: hidden;
  }
  body {
    background: var(--backdrop);
    font-family: "Arimo", Arial, sans-serif;
    color: var(--ink-light);
    display: flex;
    flex-direction: column;
    align-items: center;
    justify-content: center;
    gap: 60px;
  }
  .card {
    position: relative;
    width: 600px;
    height: 340px;
    overflow: hidden;
    box-shadow: 0 10px 30px rgba(20, 40, 80, 0.25);
  }
  .card--front {
    background: linear-gradient(210deg, var(--sky) 0%, var(--navy) 55%, var(--navy-deep) 100%);
  }
  .card--back {
    background: linear-gradient(200deg, var(--sky-light) 0%, var(--sky) 30%, var(--navy) 65%, var(--navy-deep) 100%);
  }

  /* Brand lockup */
  .brand {
    position: absolute;
    display: flex;
    align-items: center;
    gap: 10px;
    font-weight: 400;
    color: var(--ink-light);
  }
  .brand__name {
    text-transform: uppercase;
    line-height: 1.1;
  }
  .brand__mark {
    border-radius: 50%;
    background: var(--orb);
    flex: none;
  }
  .card--front .brand { top: 22px; right: 30px; }
  .card--front .brand__name { font-size: 15px; letter-spacing: 4px; text-align: center; }
  .card--front .brand__tag { display: block; font-size: 7px; letter-spacing: 3px; }
  .card--front .brand__mark { width: 54px; height: 54px; }

  .card--back .brand { top: 118px; left: 80px; gap: 16px; }
  .card--back .brand__name { font-size: 38px; letter-spacing: 14px; text-align: center; }
  .card--back .brand__tag { display: block; font-size: 12px; letter-spacing: 9px; margin-top: 4px; }
  .card--back .brand__mark { width: 110px; height: 110px; }

  /* Front details */
  .office {
    position: absolute;
    left: 58px;
    top: 210px;
  }
  .office__title {
    font-size: 25px;
    font-weight: 700;
    margin-bottom: 4px;
  }
  .office__line {
    font-size: 15px;
    line-height: 1.35;
    color: var(--ink-soft);
  }
  .contact {
    position: absolute;
    left: 372px;
    top: 210px;
    font-size: 12.5px;
    line-height: 1.45;
    color: var(--ink-soft);
  }
  .divider {
    position: absolute;
    left: 0;
    top: 0;
    width: 600px;
    height: 340px;
  }
</style>
</head>
<body>

  <section class="card card--front" aria-label="Business card front">
    <div class="brand">
      <div class="brand__name">Marrick<span class="brand__tag">Global Logistics</span></div>
      <span class="brand__mark" aria-hidden="true"></span>
    </div>

    <div class="office">
      <h1 class="office__title">General Enquiries</h1>
      <p class="office__line">57 Tidewater Street</p>
      <p class="office__line">Eastmere NSW 2011</p>
    </div>

    <div class="contact">
      <p>Email: info@marrick.com.au</p>
      <p>Phone; +61 2 5550 4182</p>
      <p>www.marrick.com.au</p>
    </div>

    <svg class="divider" viewBox="0 0 600 340" aria-hidden="true">
      <line x1="0" y1="300" x2="600" y2="252" stroke="var(--rule)" stroke-width="2"/>
    </svg>
  </section>

  <section class="card card--back" aria-label="Business card back">
    <div class="brand">
      <div class="brand__name">Marrick<span class="brand__tag">Global Logistics</span></div>
      <span class="brand__mark" aria-hidden="true"></span>
    </div>
  </section>

</body>
</html>
```